Business Card Design Project

Cyber Security. Company name is brightHarbor.

Industry/Entity Type

Computer Security

Contact Information for Business Card

Gregory Lindqvist
Founder and Chief Hacker

2370 W. Alder Rd.
Suite 514
Chicago, IL 60482
773.555.0196
gregory.lindqvist@brightharbor.example
www.brightharbor.example

```html
<!DOCTYPE html>
<html lang="en">
<head>
<meta charset="utf-8">
<title>brightHarbor business card</title>
<link rel="stylesheet" href="https://fonts.googleapis.com/css2?family=Roboto:wght@400;500;700&family=Open+Sans:wght@400&display=swap">
<style>
  :root {
    --page-bg: #e6e7ea;
    --card-dark: #2e3547;
    --card-light: #ffffff;
    --ink: #111111;
    --ink-soft: #222222;
    --accent-blue: #1e8fd4;
    --logo-blue: #6a80c8;
    --band-red: #ef5a2f;
    --band-orange: #f8a51c;
    --band-blue-dark: #1a6fb8;
    --band-blue: #2aa0dd;
  }
  * { box-sizing: border-box; margin: 0; padding: 0; }
  html, body { width: 1200px; height: 904px; overflow: hidden; }
  body {
    background: var(--page-bg);
    font-family: "Roboto", Arial, sans-serif;
    color: var(--ink);
    position: relative;
  }
  .card {
    position: absolute;
    left: 300px;
    width: 600px;
    height: 343px;
    border-radius: 22px;
    overflow: hidden;
    box-shadow: 0 6px 18px rgba(0,0,0,0.18);
  }
  .card--front { top: 90px; background: var(--card-dark); }
  .card--back { top: 471px; background: var(--card-light); }

  .wordmark {
    display: flex;
    align-items: center;
    gap: 12px;
  }
  .wordmark__dot {
    width: 46px; height: 46px;
    border-radius: 50%;
    background: var(--logo-blue);
    flex: none;
  }
  .wordmark__name {
    font-family: "Open Sans", Arial, sans-serif;
    font-weight: 400;
    font-size: 52px;
    letter-spacing: 0.5px;
    line-height: 1;
    white-space: nowrap;
  }
  .card--front .wordmark {
    position: absolute;
    left: 50%; top: 50%;
    transform: translate(-50%, -50%);
  }
  .card--front .wordmark__name { color: #ffffff; }

  .card--back .wordmark {
    position: absolute;
    left: 30px; top: 108px;
  }
  .card--back .wordmark__dot { width: 36px; height: 36px; }
  .card--back .wordmark__name { font-size: 38px; color: var(--logo-blue); }

  .divider {
    position: absolute;
    left: 26px; right: 28px; top: 160px;
    height: 1.5px;
    background: var(--ink);
  }

  .person {
    position: absolute;
    right: 32px; top: 52px;
    text-align: left;
  }
  .person__name {
    font-weight: 700;
    font-size: 25px;
    letter-spacing: 0.3px;
    color: var(--ink);
    white-space: nowrap;
  }
  .person__title {
    font-weight: 500;
    font-size: 16px;
    color: var(--accent-blue);
    margin-top: 2px;
    letter-spacing: 0.3px;
    white-space: nowrap;
  }

  .address {
    position: absolute;
    right: 32px; top: 176px;
    text-align: right;
    font-size: 16px;
    line-height: 1.5;
    color: var(--ink-soft);
  }

  .contacts {
    position: absolute;
    left: 30px; top: 176px;
    list-style: none;
    font-size: 16px;
    color: var(--ink-soft);
  }
  .contacts li {
    display: flex;
    align-items: center;
    gap: 10px;
    height: 28px;
  }
  .contacts svg { width: 15px; height: 15px; flex: none; }

  .color-band {
    position: absolute;
    left: 0; right: 0; bottom: 0;
    height: 13px;
    display: flex;
  }
  .color-band__warm {
    flex: 0 0 68%;
    background: linear-gradient(90deg, var(--band-red), var(--band-orange));
  }
  .color-band__cool {
    flex: 1;
    background: linear-gradient(90deg, var(--band-blue-dark), var(--band-blue));
  }
</style>
</head>
<body>

  <section class="card card--front" aria-label="Card front">
    <div class="wordmark">
      <span class="wordmark__dot"></span>
      <span class="wordmark__name">brightHarbor</span>
    </div>
  </section>

  <section class="card card--back" aria-label="Card back">
    <div class="wordmark">
      <span class="wordmark__dot"></span>
      <span class="wordmark__name">brightHarbor</span>
    </div>

    <div class="person">
      <div class="person__name">Gregory Lindqvist</div>
      <div class="person__title">Founder and Chief Hacker</div>
    </div>

    <div class="divider"></div>

    <ul class="contacts">
      <li>
        <svg viewBox="0 0 16 16" aria-hidden="true"><path fill="#1e8fd4" d="M3.6 1.2l2.3 2.6-1.3 1.7c.9 2 2.5 3.6 4.5 4.6l1.7-1.3 2.6 2.3-1.4 2.3C7 13.2 2.7 8.9 1.4 3.3z"/></svg>
        <span>773.555.0196</span>
      </li>
      <li>
        <svg viewBox="0 0 16 16" aria-hidden="true"><rect x="1" y="3" width="14" height="10" fill="#1e8fd4"/><path d="M1.5 3.5L8 9l6.5-5.5" stroke="#fff" stroke-width="1.3" fill="none"/></svg>
        <span>gregory.lindqvist@brightharbor.example</span>
      </li>
      <li>
        <svg viewBox="0 0 16 16" aria-hidden="true"><g fill="none" stroke="#1e8fd4" stroke-width="1.3"><circle cx="8" cy="8" r="6.5"/><ellipse cx="8" cy="8" rx="2.8" ry="6.5"/><path d="M1.5 8h13M2.5 4.8h11M2.5 11.2h11"/></g></svg>
        <span>www.brightharbor.example</span>
      </li>
    </ul>

    <div class="address">
      2370 W. Alder Rd.<br>
      Suite 514, Chicago, IL 60482
    </div>

    <div class="color-band">
      <span class="color-band__warm"></span>
      <span class="color-band__cool"></span>
    </div>
  </section>

</body>
</html>
```